Business Card Design

We need a business card design for a kids clothes shop in Ireland called "Tiny Trotz". Would prefer the colours Lime Green and Dark Purple to be used but are open to suggestions. The logo should include a "Cool" penguin with clothes on.

Industry/Entity Type

Shop

Contact Information for Business Card

Tiny Trotz
Harlow Arcade,
Ashvale Road, Childrenswear 0-12yrs
Brackenmoor,
XQ82 5LW. Deirdre Walsh.

```html
<!DOCTYPE html>
<html lang="en">
<head>
<meta charset="utf-8">
<title>Tiny Trotz – Business Card</title>
<link rel="stylesheet" href="https://fonts.googleapis.com/css2?family=Patua+One&display=swap">
<style>
  :root {
    --page-bg: #e6e6e6;
    --card-white: #ffffff;
    --plum: #5e2448;
    --plum-light: #74325c;
    --lime: #6cc04a;
    --text-white: #ffffff;
    --mascot-tint: #ececec;
  }
  * { margin: 0; padding: 0; box-sizing: border-box; }
  html, body {
    width: 1200px;
    height: 900px;
    overflow: hidden;
    background: var(--page-bg);
    font-family: "Patua One", serif;
  }
  .business-card {
    position: absolute;
    left: 120px;
    top: 160px;
    width: 960px;
    height: 580px;
    border-radius: 34px;
    background: var(--card-white);
    overflow: hidden;
    box-shadow: 0 18px 40px rgba(0, 0, 0, 0.18);
  }
  .mascot-watermark {
    position: absolute;
    left: -20px;
    top: 10px;
    width: 330px;
    height: 470px;
    border-radius: 160px 160px 60px 60px;
    background: radial-gradient(ellipse at 50% 40%, var(--mascot-tint), rgba(236, 236, 236, 0));
  }
  .wave-band {
    position: absolute;
    inset: 0;
    width: 100%;
    height: 100%;
  }
  .brand-lockup {
    position: absolute;
    left: 120px;
    top: 40px;
    width: 400px;
    display: flex;
    flex-direction: column;
    align-items: center;
    gap: 20px;
  }
  .brand-dot {
    width: 140px;
    height: 140px;
    border-radius: 50%;
    background: var(--lime);
  }
  .brand-name {
    font-size: 66px;
    line-height: 1;
    color: var(--plum);
    letter-spacing: 1px;
    white-space: nowrap;
  }
  .owner-name {
    position: absolute;
    right: 452px;
    top: 440px;
    font-size: 38px;
    color: var(--lime);
    white-space: nowrap;
  }
  .divider {
    position: absolute;
    left: 530px;
    top: 384px;
    width: 2px;
    height: 140px;
    background: var(--text-white);
    opacity: 0.85;
  }
  .shop-details {
    position: absolute;
    left: 552px;
    top: 386px;
    color: var(--text-white);
    font-size: 23px;
    line-height: 1.42;
    font-style: normal;
  }
  .shop-details .tagline {
    color: var(--lime);
    font-size: 28px;
    line-height: 1.2;
    margin-bottom: 4px;
  }
</style>
</head>
<body>
  <section class="business-card" aria-label="Tiny Trotz business card">
    <div class="mascot-watermark" role="img" aria-label="Faint large mascot decoration"></div>

    <svg class="wave-band" viewBox="0 0 960 580" preserveAspectRatio="none" aria-hidden="true">
      <defs>
        <linearGradient id="plumFill" x1="0" y1="0" x2="0" y2="1">
          <stop offset="0" stop-color="#74325c"/>
          <stop offset="1" stop-color="#561f41"/>
        </linearGradient>
      </defs>
      <path d="M0 440 C320 392 620 330 960 148 L960 170 C620 334 320 396 0 442 Z" fill="#6cc04a"/>
      <path d="M0 452 C320 402 620 342 960 180 L960 580 L0 580 Z" fill="url(#plumFill)"/>
    </svg>

    <div class="brand-lockup">
      <span class="brand-dot" aria-hidden="true"></span>
      <span class="brand-name">Tiny Trotz</span>
    </div>

    <p class="owner-name">Deirdre Walsh</p>
    <span class="divider" aria-hidden="true"></span>
    <address class="shop-details">
      <p class="tagline">Childrenswear 0-12yrs</p>
      <p>Harlow Arcade, Ashvale Road,</p>
      <p>Brackenmoor,</p>
      <p>XQ82 5LW.</p>
    </address>
  </section>
</body>
</html>
```